Wedding Day Custom Wine Label - Tasmanian (Tamar Valley) wine

I am looking for a custom design that will be put on a wine label to commemorate a very good friend's wedding day.

We will need to be able to take the design and print it on to sticker labels that we can put on to wine bottles.

The bride and groom have asked for a simplistic label design (see example image attached). We need two labels. One for "Pinot Noir" wine and the other for "Chardonnay" wine. We would like the label to say:

The Drumwell's
Pinot Noir
2023
Tamar Valley

and for for the other wine variety:

The Drumwell's
Chardonnay
2023
Tamar Valley

smaller text below to say:

13.5% ALC/VOL 750ML
MAREN & JONAS - 31.10.2024

I am happy to consider other variations - the bride & groom would prefer something minimalistic. Elegant and classy.

Target Market(s)

the bride & groom

Requirements
Must have
• Wedding date (31.10.2024). Wine type (Pinot Noir or Chardonnay).
Should not have
• images not essential

```html
<!DOCTYPE html>
<html lang="en">
<head>
<meta charset="utf-8">
<title>The Drumwell's – Wedding Wine Labels</title>
<link href="https://fonts.googleapis.com/css2?family=Great+Vibes&family=Alfa+Slab+One&family=Libre+Caslon+Text:wght@400;700&display=swap" rel="stylesheet">
<style>
  :root {
    --backdrop: #ededeb;
    --label-cream: #f7f5e6;
    --ink: #111111;
    --script-grey: #97958f;
    --muted-grey: #7a7872;
  }
  * { margin: 0; padding: 0; box-sizing: border-box; }
  html, body {
    width: 1200px;
    height: 800px;
    overflow: hidden;
    background: var(--backdrop);
  }
  .label-sheet {
    width: 1200px;
    height: 800px;
    display: flex;
    justify-content: center;
    align-items: center;
    gap: 290px;
  }
  .wine-label {
    position: relative;
    width: 356px;
    height: 462px;
    background: var(--label-cream);
    text-align: center;
    overflow: hidden;
  }
  .wine-label > * {
    position: absolute;
    left: 0;
    right: 0;
    line-height: 1;
    white-space: nowrap;
  }
  .family-name {
    top: 50px;
    width: 356px;
    height: 150px;
  }
  .family-name text {
    font-family: "Great Vibes", cursive;
    font-size: 88px;
    fill: var(--script-grey);
  }
  .varietal {
    top: 217px;
    font-family: "Alfa Slab One", serif;
    font-weight: 400;
    font-size: 21px;
    letter-spacing: 1px;
    color: var(--ink);
  }
  .vintage {
    top: 242px;
    font-family: "Libre Caslon Text", serif;
    font-size: 20px;
    letter-spacing: 1px;
    color: var(--ink);
    font-variant-numeric: oldstyle-nums;
  }
  .region {
    top: 265px;
    font-family: "Libre Caslon Text", serif;
    font-weight: 700;
    font-size: 16px;
    letter-spacing: 3px;
    color: var(--muted-grey);
  }
  .couple {
    top: 326px;
    font-family: "Libre Caslon Text", serif;
    font-size: 22px;
    letter-spacing: 4px;
    color: var(--ink);
  }
  .wedding-date {
    top: 351px;
    font-family: "Libre Caslon Text", serif;
    font-size: 19px;
    letter-spacing: 1.5px;
    color: var(--ink);
    font-variant-numeric: oldstyle-nums;
  }
  .abv {
    top: 392px;
    font-family: "Libre Caslon Text", serif;
    font-size: 15px;
    color: var(--muted-grey);
    font-variant-numeric: oldstyle-nums;
  }
  .volume {
    top: 411px;
    font-family: "Libre Caslon Text", serif;
    font-size: 15px;
    color: var(--muted-grey);
    font-variant-numeric: oldstyle-nums;
  }
</style>
</head>
<body>
  <main class="label-sheet">
    <article class="wine-label wine-label--pinot">
      <h1 class="family-name">
        <svg width="356" height="150" viewBox="0 0 356 150" aria-label="The Drumwell's">
          <text x="178" y="112" text-anchor="middle" textLength="336" lengthAdjust="spacingAndGlyphs">The Drumwell's</text>
        </svg>
      </h1>
      <h2 class="varietal">PINOT NOIR</h2>
      <p class="vintage">2023</p>
      <p class="region">TAMAR VALLEY</p>
      <p class="couple">MAREN &amp; JONAS</p>
      <p class="wedding-date">31.10.2024</p>
      <p class="abv">13.5% ALC/VOL</p>
      <p class="volume">750ML</p>
    </article>
    <article class="wine-label wine-label--chardonnay">
      <h1 class="family-name">
        <svg width="356" height="150" viewBox="0 0 356 150" aria-label="The Drumwell's">
          <text x="178" y="112" text-anchor="middle" textLength="336" lengthAdjust="spacingAndGlyphs">The Drumwell's</text>
        </svg>
      </h1>
      <h2 class="varietal">CHARDONNAY</h2>
      <p class="vintage">2023</p>
      <p class="region">TAMAR VALLEY</p>
      <p class="couple">MAREN &amp; JONAS</p>
      <p class="wedding-date">31.10.2024</p>
      <p class="abv">13.5% ALC/VOL</p>
      <p class="volume">750ML</p>
    </article>
  </main>
</body>
</html>
```